TRU PEAK POWER.

I'd like my business logo.
contact name: Desmond Halvik
phone:0438275160
email: info@trupeakpower.net.au
website: www.trupeakpower.net.au

services:
solar
battery storage
LED lighting
energy saving solutions
general electrical
I'd like the design to look professional

Target Market(s)

Everyone

Industry/Entity Type

Business

Contact Information for Business Card

as described above

Requirements
Must have
• Id like the colours and the design to work well with my logo.

```html
<!DOCTYPE html>
<html lang="en">
<head>
<meta charset="utf-8">
<title>Tru Peak Power – Business Card</title>
<link href="https://fonts.googleapis.com/css2?family=Nunito:wght@600;700;800&display=swap" rel="stylesheet">
<style>
  :root {
    --lime: #8cc63e;
    --leaf: #55ab3f;
    --teal-green: #4caf78;
    --ink: #3a3a3a;
    --orange: #f7941d;
    --sun-soft: #fdd08a;
    --leaf-soft: #c9e08a;
    --mint-soft: #8fd0b0;
    --paper: #ffffff;
  }
  * { margin: 0; padding: 0; box-sizing: border-box; }
  html, body {
    width: 1200px; height: 644px; overflow: hidden;
    background: var(--paper);
    font-family: "Nunito", "Arial Rounded MT Bold", sans-serif;
  }
  .card {
    position: relative;
    width: 1200px; height: 644px;
    background: var(--paper);
    overflow: hidden;
  }
  .brand {
    position: absolute;
    left: 62px; top: 150px;
    display: flex; align-items: center; gap: 18px;
  }
  .brand-dot {
    width: 62px; height: 62px; border-radius: 50%;
    background: var(--orange);
  }
  .brand-name {
    font-size: 50px; font-weight: 800;
    color: var(--leaf);
    letter-spacing: 0.5px;
    line-height: 1;
  }
  .services {
    position: absolute; left: 78px; top: 270px;
    width: 460px;
    font-size: 25px; font-weight: 700; line-height: 1;
  }
  .service { position: absolute; white-space: nowrap; }
  .service.lime { color: var(--lime); }
  .service.leaf { color: var(--leaf); }
  .s-solar   { left: 0;   top: 5px; }
  .s-led     { left: 220px; top: 5px; }
  .s-battery { left: 2px; top: 44px; }
  .s-saving  { left: 260px; top: 44px; }
  .contact-name {
    position: absolute; left: 80px; top: 376px;
    font-size: 28px; font-weight: 800;
    color: var(--teal-green);
  }
  .contacts {
    position: absolute; left: 77px; top: 436px;
    list-style: none;
  }
  .contact {
    display: flex; align-items: center; gap: 14px;
    height: 26px; margin-bottom: 26px;
    font-size: 18px; font-weight: 700; color: var(--ink);
  }
  .contact-icon {
    width: 27px; height: 27px; border-radius: 6px;
    background: var(--orange);
    display: flex; align-items: center; justify-content: center;
    flex: none;
  }
  .contact-icon svg { width: 16px; height: 16px; }
  .emblem-area {
    position: absolute; left: 640px; top: 10px;
    width: 540px; height: 575px;
    border-radius: 48% 48% 30% 30%;
    background: radial-gradient(circle at 60% 62%, var(--leaf-soft) 0%, var(--mint-soft) 35%, var(--sun-soft) 62%, rgba(255,255,255,0) 78%);
    opacity: 0.75;
  }
  .base-band {
    position: absolute; left: 0; bottom: 0;
    width: 1200px; height: 18px;
    background: var(--orange);
  }
</style>
</head>
<body>
  <main class="card">
    <div class="brand">
      <span class="brand-dot"></span>
      <span class="brand-name">TRU PEAK POWER</span>
    </div>

    <div class="services">
      <span class="service lime s-solar">solar</span>
      <span class="service lime s-led">LED lighting energy</span>
      <span class="service leaf s-battery">battery storage</span>
      <span class="service leaf s-saving">saving solutions</span>
    </div>

    <h1 class="contact-name">Desmond Halvik</h1>

    <ul class="contacts">
      <li class="contact">
        <span class="contact-icon">
          <svg viewBox="0 0 16 16" aria-hidden="true"><path fill="#fff" d="M3.6 1.5l2.2 2.6-1.2 1.6c.9 2 2.6 3.7 4.6 4.6l1.6-1.2 2.6 2.2-1.2 2.2C7 13.2 2.8 9 1.4 2.7z"/></svg>
        </span>
        <span>0438275160</span>
      </li>
      <li class="contact">
        <span class="contact-icon">
          <svg viewBox="0 0 16 16" aria-hidden="true"><rect x="2" y="4" width="12" height="8.5" rx="1" fill="#fff"/><path d="M2.5 4.5L8 9l5.5-4.5" fill="none" stroke="#f7941d" stroke-width="1.2"/></svg>
        </span>
        <span>info@trupeakpower.net.au</span>
      </li>
      <li class="contact">
        <span class="contact-icon">
          <svg viewBox="0 0 16 16" aria-hidden="true"><g fill="none" stroke="#fff" stroke-width="1.3"><circle cx="8" cy="8" r="6"/><ellipse cx="8" cy="8" rx="2.6" ry="6"/><path d="M2 8h12M3 5h10M3 11h10"/></g></svg>
        </span>
        <span>www.trupeakpower.net.au</span>
      </li>
    </ul>

    <div class="emblem-area" role="img" aria-label="Large faint brand emblem in soft sun orange and leaf green"></div>

    <div class="base-band"></div>
  </main>
</body>
</html>
```